KVR GUARDING WEBSITE BANNER DESIGN OF AWESOME

Please take a look at the attached Banner. I want a redesign Idea. The requirements are below.

1)Must Use Website Background
2)Must Use Photo Provided
3)Must Include Button
4)Website the banner will be used on you can see the current at the bottom of the page: https://b.pelmarox.com

Target Market(s)

Anyone Seeking Security Guard Services

```html
<!DOCTYPE html>
<html lang="en">
<head>
<meta charset="utf-8">
<title>KVR Guarding – Get Secured Today</title>
<link rel="stylesheet" href="https://fonts.googleapis.com/css2?family=Poppins:wght@400;500;600&family=Roboto+Condensed:wght@400;500;600&family=Kumbh+Sans:wght@600&display=swap">
<style>
  :root {
    --amber: #f7b223;
    --amber-deep: #f5a50f;
    --ink: #1b1b1b;
    --nav-top: #1f2a36;
    --nav-bottom: #1d5184;
    --banner-light: #22578a;
    --banner-dark: #163a66;
    --banner-band: #1b3f6e;
    --white: #ffffff;
    --cream: #fdf6e8;
    --navy: #14284a;
    --tick: #e8d53c;
    --photo-light: #8e9db0;
    --photo-dark: #1a2432;
  }
  * { box-sizing: border-box; margin: 0; padding: 0; }
  html, body { width: 1200px; height: 477px; overflow: hidden; }
  body {
    position: relative;
    font-family: "Poppins", sans-serif;
    background: linear-gradient(180deg, var(--nav-top) 0px, var(--nav-top) 40px, var(--nav-bottom) 160px, var(--banner-dark) 477px);
  }

  .announcement {
    position: absolute; left: 0; top: 0; width: 1200px; height: 31px;
    background: var(--amber);
    color: var(--ink);
    font-size: 13.5px; font-weight: 500;
    display: flex; align-items: center; justify-content: flex-end;
    padding-right: 48px;
  }
  .announcement .learn-more { color: #6b3a00; font-weight: 600; margin-left: 4px; }

  .site-nav { position: absolute; left: 0; top: 31px; width: 1200px; height: 112px; }
  .brand {
    position: absolute; left: 44px; top: 34px;
    display: flex; align-items: center; gap: 8px;
    color: var(--white); font-size: 17px; font-weight: 600; letter-spacing: 0.5px;
  }
  .brand-dot { width: 14px; height: 14px; border-radius: 50%; background: var(--amber); }
  .nav-link {
    position: absolute; top: 37px;
    color: var(--white); font-size: 14.5px; font-weight: 400;
    white-space: nowrap; display: flex; align-items: center; gap: 6px;
  }
  .nav-link.is-active { color: var(--amber); }
  .nav-link svg { width: 9px; height: 6px; }
  .nav-divider { position: absolute; left: 960px; top: 38px; width: 1px; height: 22px; background: rgba(255,255,255,0.4); }
  .quote-button {
    position: absolute; left: 966px; top: 26px; width: 156px; height: 39px;
    border-radius: 20px; background: var(--amber-deep);
    color: var(--ink); font-size: 14px; font-weight: 500;
    display: flex; align-items: center; justify-content: center;
  }

  .hero {
    position: absolute; left: 4px; top: 146px; width: 1191px; height: 329px;
    border: 1px solid rgba(255,255,255,0.85);
    overflow: hidden;
    background: linear-gradient(160deg, var(--banner-light) 0%, var(--banner-dark) 100%);
  }
  .hero-shapes, .hero-photo { position: absolute; left: 0; top: 0; }
  .hero-watermark {
    position: absolute; left: 950px; top: 120px;
    color: rgba(255,255,255,0.07); font-family: "Roboto Condensed", sans-serif;
    font-size: 40px; font-weight: 600; letter-spacing: 2px;
  }
  .hero-copy {
    position: absolute; left: 620px; top: 60px; width: 360px; text-align: center;
    font-family: "Roboto Condensed", sans-serif; color: var(--white);
  }
  .hero-title { font-size: 47px; font-weight: 500; line-height: 1; letter-spacing: 0.3px; }
  .hero-subtitle { font-size: 27px; font-weight: 500; margin-top: 12px; line-height: 1; }
  .cta-button {
    position: absolute; left: 707px; top: 183px; width: 180px; height: 42px;
    background: var(--cream); border-radius: 5px;
    box-shadow: 3px 3px 4px rgba(0,0,0,0.35);
    color: var(--navy); font-family: "Kumbh Sans", sans-serif; font-size: 28px; font-weight: 600;
    display: flex; align-items: center; justify-content: center;
  }
  .feature-list {
    position: absolute; left: 554px; top: 266px; list-style: none;
    display: flex; gap: 26px;
    font-family: "Roboto Condensed", sans-serif; font-size: 20.5px; font-weight: 500; color: var(--white);
  }
  .feature-list li { display: flex; align-items: center; gap: 4px; }
  .feature-list svg { width: 14px; height: 14px; }
</style>
</head>
<body>
  <div class="announcement">Now available! Live Monitoring Services, Deter Crime and Secure your property at a fraction of the cost of Physical Security Guards.<span class="learn-more">Learn More→</span></div>

  <header class="site-nav">
    <div class="brand"><span class="brand-dot"></span>KVR GUARDING</div>
    <a class="nav-link is-active" style="left:258px">HOME</a>
    <a class="nav-link" style="left:329px">ABOUT US</a>
    <a class="nav-link" style="left:429px">SERVICES <svg viewBox="0 0 9 6"><path d="M0 0 L9 0 L4.5 6 Z" fill="#fff"/></svg></a>
    <a class="nav-link" style="left:542px">EMPLOYMENT</a>
    <a class="nav-link" style="left:711px">CONTACT US <svg viewBox="0 0 9 6"><path d="M0 0 L9 0 L4.5 6 Z" fill="#fff"/></svg></a>
    <a class="nav-link" style="left:852px">CLIENT LOGIN</a>
    <span class="nav-divider"></span>
    <a class="quote-button">REQUEST A QUOTE</a>
  </header>

  <section class="hero">
    <svg class="hero-shapes" width="1191" height="329" viewBox="0 0 1191 329">
      <polygon points="300,329 1191,150 1191,329" fill="var(--banner-band)" opacity="0.8"/>
      <polygon points="560,200 1191,60 1191,110 560,260" fill="#ffffff" opacity="0.03"/>
    </svg>
    <svg class="hero-photo" width="1191" height="329" viewBox="0 0 1191 329" role="img" aria-label="Security guard shining a flashlight up a dark stairwell">
      <defs>
        <linearGradient id="photoTone" x1="0" y1="0" x2="1" y2="1">
          <stop offset="0" stop-color="var(--photo-light)"/>
          <stop offset="0.55" stop-color="#4c5c72"/>
          <stop offset="1" stop-color="var(--photo-dark)"/>
        </linearGradient>
      </defs>
      <polygon points="0,0 583,0 583,222 310,300 0,329" fill="url(#photoTone)"/>
    </svg>
    <div class="hero-watermark">KVR GUARDING</div>

    <div class="hero-copy">
      <h1 class="hero-title">Get Secured Today</h1>
      <p class="hero-subtitle">We take your security personal.</p>
    </div>
    <a class="cta-button">Get Started</a>

    <ul class="feature-list">
      <li><svg viewBox="0 0 14 14"><rect x="1" y="3" width="10" height="10" fill="none" stroke="var(--tick)" stroke-width="1.6"/><path d="M3 7 L6 10 L13 1" fill="none" stroke="var(--tick)" stroke-width="2"/></svg>Client Portal</li>
      <li><svg viewBox="0 0 14 14"><rect x="1" y="3" width="10" height="10" fill="none" stroke="var(--tick)" stroke-width="1.6"/><path d="M3 7 L6 10 L13 1" fill="none" stroke="var(--tick)" stroke-width="2"/></svg>24x7 Dispatch</li>
      <li><svg viewBox="0 0 14 14"><rect x="1" y="3" width="10" height="10" fill="none" stroke="var(--tick)" stroke-width="1.6"/><path d="M3 7 L6 10 L13 1" fill="none" stroke="var(--tick)" stroke-width="2"/></svg>No Binding Contracts</li>
    </ul>
  </section>
</body>
</html>
```